HTML Vorlage für Newsletter von kurortfinder18.de
Zielgruppe
Die Firma marvando GmbH & Co. KG betreibt mit https://www.kurortfinder18.de eine Wellnesshotel Buchungsplattform auf der Erholungssuchende einfach und schnell passende Angebote finden und buchen können.
Für kurortfinder18.de benötigen wir nun eine Design / HTML-Newslettervorlage welche wir zukünftig einsetzen werden.
Aufgabenstellung
Der Aufbau:
Im oberen Bereich sollte sich ein größeres Freifeld befinden, welches wir bei Bedarf mit individuellen Inhalten füllen. Bitte beim Konzept beachten, dass der Bereich nicht immer gefüllt ist und auch leer sein kann (dies wird dann in der Programmierung gesteuert), der Bereich sollte also auch ansprechend aussehen, wenn er nicht gefüllt ist.
Um mittleren Bereich folgen dann untereinander stehend ca. 10 Angebote (mit Arrangementname, Bild, Kurzbeschreibung und Link) aus unserem Portfolio die mir einem optisch schönen "Trenner" zwischen den Angeboten versehen werden sollen.
Im unteren Bereich sollten dann Abmeldelink und Impressum positioniert werden.
Im gesamten soll der Newsletter nicht zu verspielt sein, sondern eher schlicht, aber modern und entsprechend unserer Zielgruppe gestaltet sein.
Auf Anfragen können wir gerne einen Newsletter, der in etwa in die Richtung unserer Vorstellungen geht zusenden.
Bitte CI / CD & Stylguide unbedingt beachten.
Die uneingeschränkten Nutzungsrechte muss nach Abnahme an uns über gehen.
Sollte das Preisgeld zu niedrig angesetzt sein, da wir den Aufwand nicht 100 % einschätzen können, weisen Sie uns bitte darauf hin.
Da wir das Datenformat, welches geliefert werden soll, hier nicht abändern können, hier noch einmal der Hinweis, dass wir die Lieferung als fertiges HTML benötigen. In Ausnahmefällen würde uns die PSD als Gesamtansicht und die einzelnen Grafiken als JPG auch ausreichen. Bevorzugt aber natürlich das fertige HTML.

```html
<!DOCTYPE html>
<html lang="de">
<head>
<meta charset="utf-8">
<title>kurortfinder18.de Newsletter</title>
<link href="https://fonts.googleapis.com/css2?family=Arimo:wght@400;700&display=swap" rel="stylesheet">
<style>
  :root {
    --bg-cream: #fde59e;
    --white: #ffffff;
    --orange: #f39c1f;
    --orange-band: #f29a22;
    --violet: #a955c4;
    --dark: #222222;
    --green: #2f7d1e;
  }
  * { box-sizing: border-box; margin: 0; padding: 0; }
  html, body { width: 1200px; height: 3724px; overflow: hidden; }
  body {
    position: relative;
    background: var(--bg-cream);
    font-family: "Arimo", Arial, sans-serif;
  }
  .side-column {
    position: absolute; left: 104px; top: 0;
    width: 390px; height: 3670px;
    background: var(--white);
  }
  .brand {
    position: absolute; left: 136px; top: 46px;
    display: flex; align-items: center; gap: 14px;
    color: var(--orange); font-size: 38px; font-weight: 400;
  }
  .brand-dot { width: 40px; height: 40px; border-radius: 50%; background: var(--orange); }
  .hero {
    position: absolute; left: 74px; top: 186px; width: 1050px;
  }
  .hero-photo {
    height: 536px;
    background: linear-gradient(180deg, #6d8f5a 0%, #4d7a34 45%, #6fae3a 70%, #5f9b2f 100%);
    position: relative;
  }
  .hero-badge {
    position: absolute; left: 348px; top: 158px;
    width: 392px; height: 222px; background: var(--white);
    display: flex; flex-direction: column; align-items: center; justify-content: center; gap: 16px;
  }
  .hero-badge .brand-dot { width: 80px; height: 80px; }
  .hero-badge-name { color: var(--orange); font-size: 44px; }
  .hero-free-field { height: 188px; background: var(--orange-band); }

  .offer { position: absolute; left: 0; width: 1200px; height: 220px; }
  .offer-photo {
    position: absolute; left: 146px; top: 0; width: 316px; height: 212px; overflow: hidden;
  }
  .photo-dinner { background: linear-gradient(135deg, #3a2a22 0%, #6b4a38 50%, #c9a58a 75%, #7a1c24 100%); }
  .photo-spa { background: linear-gradient(160deg, #3fb9d8 0%, #5a4aa8 45%, #2c3b8c 75%, #c9a24a 100%); }
  .photo-night { background: linear-gradient(180deg, #101a3a 0%, #1d2c5a 50%, #5a5a70 70%, #0c1224 100%); }
  .price-tag {
    position: absolute; right: 0; bottom: 18px;
    min-width: 126px; padding: 6px 12px 6px 22px;
    background: var(--orange); border-radius: 30px 0 0 30px;
    color: var(--white); font-weight: 700; font-size: 20px; line-height: 24px; text-align: right;
  }
  .price-old { text-decoration: line-through; }
  .price-new { color: var(--green); display: block; }
  .offer-text { position: absolute; left: 526px; top: 14px; width: 620px; }
  .offer-title { color: var(--orange); font-size: 46px; font-weight: 400; line-height: 56px; }
  .offer-desc {
    color: var(--violet); font-size: 26px; line-height: 28px; letter-spacing: 0.6px; margin-top: 4px;
  }
  .offer-button {
    display: inline-block; margin: 14px 0 0 164px;
    padding: 3px 12px; border-radius: 18px;
    background: var(--orange); color: var(--white); font-size: 21px; line-height: 28px;
    text-decoration: none;
  }

  .footer {
    position: absolute; left: 0; top: 3670px; width: 1200px; height: 54px;
    background: var(--white);
    font-size: 18px; color: var(--dark);
  }
  .social { position: absolute; left: 240px; top: 14px; display: flex; gap: 6px; }
  .social span { width: 34px; height: 34px; border-radius: 50%; background: var(--dark); display: block; }
  .copyright { position: absolute; left: 510px; top: 16px; letter-spacing: 0.5px; }
  .legal-links { position: absolute; left: 936px; top: 20px; letter-spacing: 0.5px; }
  .legal-links a { color: var(--dark); text-decoration: none; }
</style>
</head>
<body>
  <div class="side-column"></div>

  <div class="brand"><span class="brand-dot"></span>kurortfinder18</div>

  <section class="hero">
    <div class="hero-photo" role="img" aria-label="Hotelgarten mit Liegen auf grüner Wiese vor Bergkulisse">
      <div class="hero-badge">
        <span class="brand-dot"></span>
        <span class="hero-badge-name">kurortfinder18</span>
      </div>
    </div>
    <div class="hero-free-field"></div>
  </section>

  <main class="offers">
    <article class="offer" style="top:1018px">
      <div class="offer-photo photo-dinner" role="img" aria-label="Paar beim Abendessen bei Kerzenschein"><span class="price-tag">ab 149 €</span></div>
      <div class="offer-text"><h2 class="offer-title">Angebot</h2><p class="offer-desc">Mit diesem Arrangement können Sie Ihre<br>Zeit zu Zweit im Thüringer Wald ganz bewusst<br>erleben. Denn hier lautet die Devise: verwöhnen</p><a class="offer-button" href="https://www.kurortfinder18.de">Mehr erfahren</a></div>
    </article>
    <article class="offer" style="top:1284px">
      <div class="offer-photo photo-spa" role="img" aria-label="Beleuchteter Wellnessbereich mit Brunnen"><span class="price-tag"><span class="price-old">ab 246 €</span><span class="price-new">169 €</span></span></div>
      <div class="offer-text"><h2 class="offer-title">Angebot</h2><p class="offer-desc">Mit diesem Arrangement können Sie Ihre<br>Zeit zu Zweit im Thüringer Wald ganz bewusst<br>erleben. Denn hier lautet die Devise: verwöhnen</p><a class="offer-button" href="https://www.kurortfinder18.de">Mehr erfahren</a></div>
    </article>
    <article class="offer" style="top:1550px">
      <div class="offer-photo photo-night" role="img" aria-label="Hotel am See bei Nacht"><span class="price-tag">ab 95 €</span></div>
      <div class="offer-text"><h2 class="offer-title">Angebot</h2><p class="offer-desc">Mit diesem Arrangement können Sie Ihre<br>Zeit zu Zweit im Thüringer Wald ganz bewusst<br>erleben. Denn hier lautet die Devise: verwöhnen</p><a class="offer-button" href="https://www.kurortfinder18.de">Mehr erfahren</a></div>
    </article>
    <article class="offer" style="top:1816px">
      <div class="offer-photo photo-dinner" role="img" aria-label="Paar beim Abendessen bei Kerzenschein"><span class="price-tag">ab 149 €</span></div>
      <div class="offer-text"><h2 class="offer-title">Angebot</h2><p class="offer-desc">Mit diesem Arrangement können Sie Ihre<br>Zeit zu Zweit im Thüringer Wald ganz bewusst<br>erleben. Denn hier lautet die Devise: verwöhnen</p><a class="offer-button" href="https://www.kurortfinder18.de">Mehr erfahren</a></div>
    </article>
    <article class="offer" style="top:2082px">
      <div class="offer-photo photo-spa" role="img" aria-label="Beleuchteter Wellnessbereich mit Brunnen"><span class="price-tag"><span class="price-old">ab 246 €</span><span class="price-new">169 €</span></span></div>
      <div class="offer-text"><h2 class="offer-title">Angebot</h2><p class="offer-desc">Mit diesem Arrangement können Sie Ihre<br>Zeit zu Zweit im Thüringer Wald ganz bewusst<br>erleben. Denn hier lautet die Devise: verwöhnen</p><a class="offer-button" href="https://www.kurortfinder18.de">Mehr erfahren</a></div>
    </article>
    <article class="offer" style="top:2348px">
      <div class="offer-photo photo-night" role="img" aria-label="Hotel am See bei Nacht"><span class="price-tag">ab 95 €</span></div>
      <div class="offer-text"><h2 class="offer-title">Angebot</h2><p class="offer-desc">Mit diesem Arrangement können Sie Ihre<br>Zeit zu Zweit im Thüringer Wald ganz bewusst<br>erleben. Denn hier lautet die Devise: verwöhnen</p><a class="offer-button" href="https://www.kurortfinder18.de">Mehr erfahren</a></div>
    </article>
    <article class="offer" style="top:2614px">
      <div class="offer-photo photo-dinner" role="img" aria-label="Paar beim Abendessen bei Kerzenschein"><span class="price-tag">ab 149 €</span></div>
      <div class="offer-text"><h2 class="offer-title">Angebot</h2><p class="offer-desc">Mit diesem Arrangement können Sie Ihre<br>Zeit zu Zweit im Thüringer Wald ganz bewusst<br>erleben. Denn hier lautet die Devise: verwöhnen</p><a class="offer-button" href="https://www.kurortfinder18.de">Mehr erfahren</a></div>
    </article>
    <article class="offer" style="top:2880px">
      <div class="offer-photo photo-spa" role="img" aria-label="Beleuchteter Wellnessbereich mit Brunnen"><span class="price-tag"><span class="price-old">ab 246 €</span><span class="price-new">169 €</span></span></div>
      <div class="offer-text"><h2 class="offer-title">Angebot</h2><p class="offer-desc">Mit diesem Arrangement können Sie Ihre<br>Zeit zu Zweit im Thüringer Wald ganz bewusst<br>erleben. Denn hier lautet die Devise: verwöhnen</p><a class="offer-button" href="https://www.kurortfinder18.de">Mehr erfahren</a></div>
    </article>
    <article class="offer" style="top:3146px">
      <div class="offer-photo photo-night" role="img" aria-label="Hotel am See bei Nacht"><span class="price-tag">ab 95 €</span></div>
      <div class="offer-text"><h2 class="offer-title">Angebot</h2><p class="offer-desc">Mit diesem Arrangement können Sie Ihre<br>Zeit zu Zweit im Thüringer Wald ganz bewusst<br>erleben. Denn hier lautet die Devise: verwöhnen</p><a class="offer-button" href="https://www.kurortfinder18.de">Mehr erfahren</a></div>
    </article>
    <article class="offer" style="top:3412px">
      <div class="offer-photo photo-dinner" role="img" aria-label="Paar beim Abendessen bei Kerzenschein"><span class="price-tag">ab 149 €</span></div>
      <div class="offer-text"><h2 class="offer-title">Angebot</h2><p class="offer-desc">Mit diesem Arrangement können Sie Ihre<br>Zeit zu Zweit im Thüringer Wald ganz bewusst<br>erleben. Denn hier lautet die Devise: verwöhnen</p><a class="offer-button" href="https://www.kurortfinder18.de">Mehr erfahren</a></div>
    </article>
  </main>

  <footer class="footer">
    <div class="social" aria-label="Soziale Netzwerke"><span></span><span></span><span></span></div>
    <p class="copyright">Copyright kurortfinder18.de 2017</p>
    <p class="legal-links"><a href="https://www.kurortfinder18.de">Abmelden</a> | <a href="https://www.kurortfinder18.de">Impressum</a></p>
  </footer>
</body>
</html>
```